An international recruitment business looking to attract new engineering and construction clients i

BK Worldwide is an international recruitment company with a wealth of experienced engineers, quantity surveyors and construction specialists appropriate to fill roles in the vastly growing Middle East. We need a new, attractive brochure design to send to new clients/companies so they will be interested in our recruitment company and our candidates. We have provided our company logo which we would like to feature, and we would like the theme to match this to some extent. We have also attached our current brochure which should be used for the general content and information. PLEASE NOTE: Ignore the appraisals on the penultimate page - I will provide new ones in a separate document. (Use the one with 5 appraisals, not 3!)
The final design should be modern and attractive and should feature some images of the Middle East including some impressive buildings and new railways (similar to our current ones).
Please also link our website
and use it for inspiration: http://www.bk-worldwide.co.uk
Updates
We would like the brochure to be A5 and landscape - although it will only be emailed to clients and not printed.
There is no limit on number of pages.
There seems to be a problem opening the appraisals document I attached.
The content of this document is:
BK Worldwide Appraisals
"I had the pleasure of working with BK Worldwide as a client and found them to be a great recruiter with in-depth rail knowledge, I had great results from them time after time. I found the team very trustworthy, professional and fun to work with. I would highly recommend BK Worldwide and will continue to use the company for all my future recruitment needs"
Tarek Olivastro, Dunemark Transit Company
“When looking to advance my career, I enquired with BK Worldwide about a senior position in the Middle East. I dealt specifically with Colin who I found very helpful. He informed me of all the job requirements, the background of the role, responsibilities and package. Colin was extremely diligent in moving the process forward and throughout kept in contact and abreast of the situation. In all it proved a great success and I am now happily placed in my new role. Even though Colin performed beyond the normal boundaries of his role he even now keeps in contact to make sure everything is ok and all parties happy and satisfied with the outcome. I wholeheartedly endorse Colin and BK Worldwide and will use them when I am next supplementing my team.”
Miles Thornbury, Head of Quantity Surveying, Vellum Gulf Design Partners (VGDP), Kuwait
BK Worldwide is a recruitment company that has an insatiable appetite for understanding the jobs, for which they recruit, and not only the jobs, but they also establish excellent rapport with the clients and candidates. They are always there when I need to fill positions in my organization quickly. They listen to what I need and always supply me with the resumes that I could review right away to start hiring who I needed - saving me time and effort. They are always able to supply me with the exact person that I need for the open position."
Nadia Faris, HR Consultant, Dunemark Transit
Target Market(s)
Professional clients in the Middle East
Industry/Entity Type
Construction
Colors
Designer to choose colors to be used in the design.
Look and feel

```html
<!DOCTYPE html>
<html lang="en">
<head>
<meta charset="utf-8">
<title>BK Worldwide — Brochure Spreads</title>
<link href="https://fonts.googleapis.com/css2?family=Source+Sans+3:ital,wght@0,400;0,600;0,700;1,700&display=swap" rel="stylesheet">
<style>
:root{
  --stage:#555555;
  --paper:#ffffff;
  --teal:#1aa98a;
  --teal-dark:#14866e;
  --teal-pale:#cfe9e3;
  --ink:#4a4a4a;
  --ink-soft:#6d6d6d;
  --photo-grey:#b9bec2;
}
*{margin:0;padding:0;box-sizing:border-box}
html,body{width:1200px;height:900px;overflow:hidden;background:var(--stage)}
body{position:relative;font-family:"Source Sans 3",Arial,sans-serif;color:var(--ink)}
.page{position:absolute;width:268px;height:190px;background:var(--paper);overflow:hidden;box-shadow:0 1px 3px rgba(0,0,0,.35)}
.page--teal{background:var(--teal);color:#fff}
.page--framed{outline:1px solid #111}
.page svg.deco{position:absolute;left:0;top:0;width:100%;height:100%}
.photo{position:absolute}
.title{position:absolute;font-weight:400;font-size:11px;color:var(--ink);letter-spacing:.1px}
.copy{position:absolute;font-size:3.6px;line-height:1.35;color:var(--ink)}
.copy p{margin-bottom:3.4px}
.copy b{font-weight:700}
.bullets{list-style:none}
.bullets li{position:relative;padding-left:9px;margin-bottom:5px}
.bullets li::before{content:"";position:absolute;left:0;top:.6px;width:5px;height:3px;border-radius:50%;background:var(--teal)}
.bullets b{font-style:italic;text-transform:uppercase}
.brand{position:absolute;display:flex;align-items:center;gap:4px;font-weight:600;color:var(--teal);white-space:nowrap}
.brand__dot{border-radius:50%;background:currentColor;display:inline-block}
.sector h4{font-size:6px;font-weight:600;line-height:1;margin-bottom:1px;color:var(--ink)}
.sector p{font-size:3.4px;line-height:1.3;margin-bottom:4px}
.quote{font-size:3.4px;line-height:1.4;font-weight:700;font-style:italic;text-align:justify;margin-bottom:2px}
.cite{font-size:3.2px;font-weight:700;text-align:right;margin-bottom:6px}
</style>
</head>
<body>

<!-- Cover -->
<section class="page" style="left:181px;top:134px;width:270px;height:189px">
  <svg class="deco" viewBox="0 0 270 189" preserveAspectRatio="none">
    <polygon points="0,72 117,189 0,189" fill="var(--teal)"/>
    <g stroke="#fff" stroke-width="1.6"><line x1="0" y1="92" x2="97" y2="189"/><line x1="0" y1="104" x2="85" y2="189"/></g>
    <g stroke="var(--teal)" stroke-width="1.6"><line x1="0" y1="62" x2="127" y2="189"/><line x1="0" y1="54" x2="135" y2="189"/></g>
  </svg>
  <div class="brand" style="left:62px;top:76px;font-size:20px"><span class="brand__dot" style="width:14px;height:14px"></span>BK Worldwide</div>
  <div class="copy" style="left:90px;top:100px;color:var(--ink-soft);letter-spacing:1px">RECRUITMENT FOR ENGINEERING AND CONSTRUCTION</div>
</section>

<!-- Expertise -->
<section class="page page--framed" style="left:468px;top:134px">
  <div class="photo" role="img" aria-label="Portrait of a consultant in a dark suit, arms folded" style="left:10px;top:58px;width:72px;height:132px;background:linear-gradient(#d9dcdf,var(--photo-grey))"></div>
  <svg class="deco" viewBox="0 0 268 190">
    <g stroke="var(--teal)" stroke-width="2"><line x1="58" y1="112" x2="136" y2="190"/><line x1="58" y1="124" x2="124" y2="190"/><line x1="58" y1="136" x2="112" y2="190"/></g>
  </svg>
  <h2 class="title" style="left:117px;top:13px">Expertise</h2>
  <div class="copy" style="left:117px;top:34px;width:146px;text-align:justify">
    <p>As a consultancy we pride ourselves in <b>taking full responsibility for providing our clients with the very best selection of professionals from across the globe.</b></p>
    <p>We currently recruit Construction &amp; Engineering Professionals from the UK, EU, Australia, New Zealand, Canada &amp; the USA to work with our prestigious clients across the Middle East.</p>
    <p>Our company prides itself on taking the time and effort <b>involved in understanding our clients</b>, their needs, their past and most importantly the future of the company and the direction it wishes to take. This information, in turn provides us with the specifications we need to find the talent required for the future of your business.</p>
    <p>We believe that research is a vital part of keeping ahead. We therefore dedicate part of our business to the continued study of Recruitment Trends, New Developments &amp; Economic Pressures that can have a major effect on where to find and source the best talent needed for you.</p>
  </div>
</section>

<!-- A service like no other -->
<section class="page" style="left:757px;top:131px">
  <div class="photo" role="img" aria-label="Maze of figures seen from above in pale teal" style="left:183px;top:0;width:85px;height:190px;background:linear-gradient(160deg,#e6f1ef,#9fc9c4 60%,#6fa9b4)"></div>
  <svg class="deco" viewBox="0 0 268 190">
    <g stroke="#fff" stroke-width="2.5"><line x1="190" y1="0" x2="190" y2="190"/><line x1="198" y1="0" x2="198" y2="190"/><line x1="206" y1="0" x2="206" y2="190"/></g>
  </svg>
  <h2 class="title" style="left:18px;top:14px">A service like no other...</h2>
  <ul class="copy bullets" style="left:20px;top:37px;width:158px;font-size:3.8px">
    <li style="margin-bottom:9px">You will benefit from the knowledge and experience of our trained consultants; with an exceptional understanding of the Industry sectors as well as the locations and cultures across the Middle East regions.</li>
    <li style="margin-bottom:9px">We aim to provide "Quality not Quantity" which is the thought process used prior to submitting any candidate to our clients.</li>
    <li style="margin-bottom:9px">Our aim is to give our clients a full, one stop recruitment service. Using in-depth knowledge of the market, we have the ability to target hard to source professionals for specific positions within your organisation.</li>
    <li>BK Worldwide is the next step for your company in ensuring progression &amp; development with the acquisition of highly skilled professionals.</li>
  </ul>
</section>

<!-- What we can offer -->
<section class="page" style="left:181px;top:331px;width:267px;height:189px">
  <h2 class="title" style="left:16px;top:13px">What we can offer</h2>
  <p class="copy" style="left:16px;top:34px;width:232px;font-size:5px;font-weight:600;color:var(--ink-soft)">We immediately recognise, through experience, that our clients are the most important component to our business.</p>
  <h3 style="position:absolute;left:40px;top:61px;font-size:6px;font-weight:600;color:var(--teal)">Our Services</h3>
  <ul class="copy bullets" style="left:42px;top:74px;width:190px">
    <li><b>Client centred approach</b> – dedicated line management, daily correspondence, speedy feedback and assurance of results.</li>
    <li><b>Expert global knowledge</b> – Major clients and operations across the Globe and majority in the Gulf Region.</li>
    <li><b>Global network</b> – Our international client and candidate network ensures we can resource the top specialists for our clients needs, with current experience from the World's most prestigious clients and projects.</li>
    <li><b>Emphasis on quality / targeted approach</b> – All candidates presented will be pre-screened and interviewed by our consultants to ensure the highest quality of service.</li>
  </ul>
</section>

<!-- Services continued -->
<section class="page" style="left:465px;top:329px">
  <ul class="copy bullets" style="left:40px;top:24px;width:200px">
    <li><b>Search and selection</b> – The only way to guarantee the best possible talent for the candidates that can't be found traditionally. Our dedicated head hunting division, guaranteed results.</li>
    <li><b>Recruitment drives</b> – Management of European recruitment events wherever we can pool in market specialists for volume recruitment. An option for all our valued clients.</li>
    <li><b>Expert consultants</b> – Our team are leaders in the recruitment field which will provide a proactive, knowledgeable service to our clients.</li>
    <li><b>Resources</b> – We use the most advanced recruitment tools and methods to ensure we remain a distance ahead of our competition, a position we are proud to retain.</li>
  </ul>
  <div class="photo" role="img" aria-label="Handshake between two professionals beside a hard hat" style="left:0;top:110px;width:268px;height:80px;background:linear-gradient(90deg,#aab5bf,#e3e6e8 45%,#c9c2a0 80%,#d9b64a)"></div>
</section>

<!-- Specialist Sectors -->
<section class="page" style="left:759px;top:328px">
  <div class="photo" role="img" aria-label="Faint architectural blueprint in pale teal" style="left:130px;top:0;width:138px;height:190px;background:linear-gradient(135deg,#fff 20%,#e4efee 60%,#c7dcdc)"></div>
  <svg class="deco" viewBox="0 0 268 190">
    <polygon points="268,60 268,190 138,190" fill="var(--teal)" opacity=".9"/>
    <g stroke="#fff" stroke-width="2"><line x1="268" y1="82" x2="160" y2="190"/><line x1="268" y1="100" x2="178" y2="190"/><line x1="268" y1="120" x2="198" y2="190"/></g>
    <g stroke="var(--teal)" stroke-width="1.8"><line x1="268" y1="0" x2="90" y2="190"/><line x1="268" y1="10" x2="100" y2="190"/><line x1="268" y1="22" x2="112" y2="190"/></g>
  </svg>
  <h2 class="title" style="left:16px;top:14px">Specialist Sectors</h2>
  <p class="copy" style="left:16px;top:34px;width:220px;font-size:4px">BK Worldwide is a consultancy that specialises in the permanent recruitment of professionals within the Construction &amp; Engineering sector.</p>
  <div class="sector" style="position:absolute;left:16px;top:55px;width:72px">
    <h4>Architecture</h4><p>new builds, regeneration, conservation, landscape architecture, urban design, masterplanning, commercial and residential work.</p>
    <h4>Construction and Building Services</h4><p>construction management, design and build, facilities management and building services.</p>
    <h4>Surveying</h4><p>building surveying, land surveying, quantity surveying, rural practice and hydrographic surveying.</p>
  </div>
  <div class="sector" style="position:absolute;left:100px;top:55px;width:74px">
    <h4>Civil and Structural Engineering</h4><p>coastal and marine, environmental, geotechnical, structural, highways, bridges, rail, tunnelling, airports, ports, transport planning, power, water, public health, risk management and project management.</p>
    <h4>Construction and Building Services</h4><p>construction management, design and build, facilities management and building services.</p>
  </div>
</section>

<!-- Proven track record -->
<section class="page page--teal" style="left:184px;top:528px">
  <div class="photo" role="img" aria-label="Glass tower facade in cool teal tones" style="left:0;top:0;width:80px;height:190px;background:linear-gradient(160deg,#d8e6ea,#8fb3bd 55%,#3f8c95);clip-path:polygon(0 0,75% 0,100% 52%,55% 100%,0 100%)"></div>
  <svg class="deco" viewBox="0 0 268 190">
    <g stroke="#fff" stroke-width="2"><line x1="0" y1="110" x2="52" y2="0"/><line x1="0" y1="128" x2="60" y2="0"/><line x1="0" y1="150" x2="70" y2="0"/></g>
  </svg>
  <h2 class="title" style="right:14px;top:14px;color:#fff">Proven track record...</h2>
  <div style="position:absolute;left:84px;top:34px;width:172px">
    <p class="quote">"I had the pleasure of working with BK Worldwide as a client and found them to be a great recruiter with in-depth rail knowledge, I had great results from them time after time. I found the team very trustworthy, professional and fun to work with. I would highly recommend BK Worldwide and will continue to use the company for all my future recruitment needs."</p>
    <p class="cite">Miles Thornbury, Head of Quantity Surveying, Vellum Gulf Design Partners (VGDP), Kuwait</p>
    <p class="quote">"I found BK Worldwide through a colleague of mine who had used their services in the past. My consultant provided me with various options based on my skills and future requirements, and they kept me informed throughout the process. They were very professional and prepared me well for interviews. I have no hesitation in recommending BK Worldwide."</p>
    <p class="cite">Tarek Olivastro, Project Manager, Corran Estates, Saudi Arabia</p>
    <p class="quote">"BK Worldwide found me a position of a design architect for a consultancy in Saudi Arabia. I found them to be a professional recruitment company, always on hand to answer any queries."</p>
    <p class="cite">Owen Halloway, Design Advisor, Sandmere Consultants</p>
  </div>
</section>

<!-- Back cover -->
<section class="page page--teal" style="left:467px;top:527px;width:269px;height:189px">
  <svg class="deco" viewBox="0 0 269 189">
    <polygon points="150,0 269,0 269,112" fill="#fff"/>
    <g stroke="#fff" stroke-width="2"><line x1="140" y1="0" x2="269" y2="122"/><line x1="130" y1="0" x2="269" y2="132"/></g>
    <g stroke="var(--teal)" stroke-width="1.8"><line x1="172" y1="0" x2="269" y2="90"/><line x1="190" y1="0" x2="269" y2="74"/></g>
  </svg>
  <div class="brand" style="left:98px;top:140px;font-size:10px;color:#fff"><span class="brand__dot" style="width:7px;height:7px"></span>BK Worldwide</div>
  <div class="copy" style="left:116px;top:154px;width:60px;color:#fff;font-size:3.2px;line-height:1.5">
    Design Quarter, London W1A<br>T: 020 7946 0123<br>E: hello@bk-worldwide.co.uk<br>www.bk-worldwide.co.uk
  </div>
</section>

</body>
</html>
```